Vacation rental Management Software company needs website and logo

We need a logo and new website design to promote our vacation rental management software. We sell the software to property owners and management company. We have existing website www.stayquill.example at the moment but it is need of upgrading. The goal is make it more professional looking and to put the emphasis on marketing the software.
Html + Css code is needed, the website must have responsive layout.
The logo must be composed by the brand "StayQuill" and eventually an image related to Vacation Rental Management
The pages that we need are the following:
1) Home Page
- must be highlighted the 2 main categories of customers (Direct Owners and Agencies/Portals)
- there must be a section where we can highlight some products, i.e. the latest or the most relevant
- there must be an introductive text
2) Page for a category of customer (owner or agency/portal)
- based on the page http://www.stayquill.example/owners/ or http://www.stayquill.example/agencies/, this page must highlight all the products available for the category selected, but must be more attractive then the existing ones (that have just text)
3) Single product page
- in that page must be explained a single product, a page example is this one: http://www.stayquill.example/owners/vacation-rental-website.html
4) Portfolio page
5) Contact page, with a contact form style
Industry/Entity Type
Software

```html
<!DOCTYPE html>
<html lang="en">
<head>
<meta charset="utf-8">
<title>StayQuill – Villa Rentals Booking Solutions</title>
<link rel="stylesheet" href="https://fonts.googleapis.com/css2?family=Lato:ital,wght@0,300;0,400;0,700;0,900;1,400&display=swap">
<style>
:root{
  --red:#b0141b;
  --red-dark:#8d0f14;
  --red-soft:#d9676b;
  --ink:#222;
  --text:#555;
  --muted:#888;
  --line:#ddd;
  --field:#efefef;
  --field-active:#a9c4e2;
  --panel:#f3f3f3;
  --dark:#2a2a2a;
  --white:#fff;
}
*{box-sizing:border-box;margin:0;padding:0}
html,body{width:1200px;height:2531px;overflow:hidden;background:var(--white)}
body{font-family:'Lato',sans-serif;color:var(--text);position:relative}
.abs{position:absolute}

/* header */
.site-header{position:absolute;left:0;top:0;width:1200px;height:95px;background:var(--white)}
.brand{position:absolute;left:164px;top:20px;display:flex;align-items:center;gap:10px}
.brand-mark{width:48px;height:48px;border-radius:50%;background:var(--red)}
.brand-name{font-size:34px;font-weight:700;color:var(--red);line-height:1}
.brand-tag{font-size:11px;color:var(--muted);margin-top:3px;display:block}
.top-links{position:absolute;right:162px;top:20px;display:flex;gap:26px;font-size:11px;text-transform:uppercase;align-items:center}
.top-links .login{color:var(--red)}
.top-links .flag{width:18px;height:11px;background:#4a5f9e;display:inline-block}
.main-nav{position:absolute;right:162px;top:60px;display:flex;gap:20px;font-size:11.5px;text-transform:uppercase;color:#333}

/* hero */
.hero{position:absolute;left:0;top:95px;width:1200px;height:411px;background:linear-gradient(180deg,#c9d9e8 0%,#e7e2d8 45%,#b9a58f 100%)}
.hero-title{position:absolute;left:170px;top:158px;line-height:1}
.hero-title .lead{font-size:27px;font-weight:400;color:#222;letter-spacing:.5px}
.hero-title .strong{font-size:37px;font-weight:900;color:var(--red);display:block;margin-top:2px}
.hero-arrow{position:absolute;top:270px;width:14px;height:40px}
.calendar{position:absolute;left:559px;top:116px;width:474px;height:390px;background:rgba(255,255,255,.82)}
.cal-head{height:52px;display:flex;align-items:center;justify-content:space-between;padding:0 22px;border-bottom:1px solid var(--line)}
.cal-month{font-size:26px;font-weight:700;color:var(--red);letter-spacing:4px}
.cal-grid{display:grid;grid-template-columns:repeat(7,1fr);padding:6px 14px 0;row-gap:2px}
.cal-grid span{height:46px;display:flex;align-items:center;justify-content:center;font-size:24px;color:#222;position:relative}
.cal-grid .dow{height:30px;font-size:16px;font-weight:700}
.cal-grid .off{color:#999}
.cal-grid .dot::after{content:"";position:absolute;bottom:3px;width:5px;height:5px;border-radius:50%;background:var(--red)}
.cal-grid .today::before{content:"";position:absolute;width:44px;height:44px;border-radius:50%;background:var(--red);z-index:-1}
.cal-grid .today{color:var(--white);z-index:0}
.cal-grid .mark::before{content:"";position:absolute;width:44px;height:44px;border-radius:50%;border:2px solid var(--red)}

/* audience cards */
.audience-band{position:absolute;left:0;top:506px;width:1200px;height:198px;background:linear-gradient(180deg,#fff,#e6e6e6)}
.audience-card{position:absolute;top:481px;width:426px;height:194px;background:var(--white);box-shadow:0 2px 6px rgba(0,0,0,.18);overflow:hidden}
.audience-card .accent{position:absolute;left:0;top:0;width:150px;height:194px}
.audience-card .icon{position:absolute;left:24px;top:40px;width:70px;height:70px;border-radius:50%;background:var(--white)}
.audience-card h3{position:absolute;left:148px;top:22px;font-size:21px;font-weight:400;color:#111}
.audience-card p{position:absolute;left:148px;top:58px;width:262px;font-size:11.5px;line-height:1.6;color:#444}
.btn-small{position:absolute;left:148px;top:142px;padding:6px 9px;font-size:10px;text-transform:uppercase;color:#333;background:var(--white);box-shadow:0 1px 3px rgba(0,0,0,.25)}

/* intro */
.intro-title{position:absolute;left:162px;top:758px;width:270px;font-size:18px;font-weight:700;color:#111;line-height:1.4}
.intro-divider{position:absolute;left:452px;top:748px}
.intro-lead{position:absolute;left:512px;top:752px;width:528px;font-size:11.5px;line-height:1.65;color:#555}
.intro-body{position:absolute;left:162px;top:852px;width:878px;font-size:11.5px;line-height:1.6;color:#555}
.intro-body p{margin-bottom:12px}

/* products */
.product{position:absolute;top:1086px;width:260px;text-align:center}
.product .pic{width:80px;height:80px;margin:0 auto;border-radius:8px}
.product h4{font-size:18px;font-weight:400;color:#111;margin-top:20px}
.product p{font-size:11px;line-height:1.65;color:#555;margin-top:14px;padding:0 20px}
.product .plus{width:26px;height:26px;border-radius:50%;background:var(--white);box-shadow:0 1px 3px rgba(0,0,0,.3);margin:12px auto 0;display:flex;align-items:center;justify-content:center}

/* testimonials */
.testimonials{position:absolute;left:0;top:1350px;width:1200px;height:320px;background:linear-gradient(180deg,#3a3a3a,#1f1f1f)}
.testimonials h2{position:absolute;top:38px;width:100%;text-align:center;font-size:18px;font-weight:700;color:var(--white)}
.testimonials .quote-mark{position:absolute;top:70px;width:100%;text-align:center;font-size:48px;color:var(--white);font-style:italic;line-height:1}
.testimonials blockquote{position:absolute;left:275px;top:118px;width:650px;text-align:center;font-size:11.5px;line-height:1.75;font-style:italic;color:#ddd}
.testimonials .avatar{position:absolute;left:576px;top:207px;width:48px;height:48px;border-radius:50%;background:#c9b6a6;border:3px solid var(--white)}
.testimonials .author{position:absolute;top:264px;width:100%;text-align:center;font-size:12px;color:var(--white)}

/* portfolio */
.portfolio-title{position:absolute;left:162px;top:1737px;font-size:18px;font-weight:700;color:#111}
.portfolio-divider{position:absolute;left:452px;top:1708px}
.portfolio-lead{position:absolute;left:512px;top:1712px;width:528px;font-size:11.5px;line-height:1.65;color:#555}
.tile{position:absolute;top:1814px;width:277px;height:141px;display:flex;align-items:center;justify-content:center;font-size:30px;font-weight:400;color:var(--white)}
.tile.light{background:#ececec;color:#1e4f97}
.tile-caption{position:absolute;top:1968px;font-size:11.5px;font-weight:700;color:#111}
.btn-center{position:absolute;left:564px;top:2013px;padding:7px 10px;font-size:10px;text-transform:uppercase;color:#333;box-shadow:0 1px 3px rgba(0,0,0,.25);background:var(--white)}
.rule{position:absolute;left:162px;top:2087px;width:878px;height:1px;background:var(--line)}

/* contact */
.contact-title{position:absolute;left:162px;top:2122px;font-size:18px;font-weight:700;color:#111}
.field{position:absolute;height:36px;background:var(--field);font-size:10px;color:#999;text-transform:uppercase;padding:12px 12px}
.field.active{background:var(--field-active);color:var(--white)}
.submit{position:absolute;left:162px;top:2422px;width:577px;height:38px;background:var(--red);color:var(--white);font-size:11px;text-transform:uppercase;display:flex;align-items:center;justify-content:center}
.contact-list{position:absolute;left:812px;top:2176px;font-size:14px;color:#555}
.contact-item{display:flex;gap:14px;align-items:flex-start;margin-bottom:22px;line-height:1.5}
.contact-item svg{flex:none;margin-top:2px}
.socials{display:flex;gap:6px;margin-left:38px}
.socials span{width:24px;height:24px;background:#3b6fb6}
.socials span:nth-child(2){background:#43a8e0}
.socials span:nth-child(3){background:#2a77b3}

.site-footer{position:absolute;left:0;top:2495px;width:1200px;height:36px;background:#ececec;font-size:11px;color:#555;display:flex;align-items:center;justify-content:center}
</style>
</head>
<body>

<header class="site-header">
  <div class="brand">
    <div class="brand-mark"></div>
    <div><span class="brand-name">StayQuill</span><span class="brand-tag">Villa Rentals Booking Solutions</span></div>
  </div>
  <div class="top-links"><span class="login">Owner Login</span><span>Register Now</span><span class="flag"></span></div>
  <nav class="main-nav"><span>Home</span><span>Products</span><span>Portfolio</span><span>Owners</span><span>Contact Us</span></nav>
</header>

<section class="hero" role="img" aria-label="Photograph of a white weatherboard house with a red roof under a blue sky"></section>
<div class="hero-title"><span class="lead">THE RIGHT WAY TO</span><span class="strong">MANAGE<br>RESERVATIONS</span></div>
<svg class="hero-arrow" style="left:108px" viewBox="0 0 14 40"><path d="M12 2 2 20l10 18" fill="none" stroke="#fff" stroke-width="2.5"/></svg>
<svg class="hero-arrow" style="left:1078px" viewBox="0 0 14 40"><path d="M2 2l10 18L2 38" fill="none" stroke="#fff" stroke-width="2.5"/></svg>

<div class="calendar">
  <div class="cal-head">
    <svg width="10" height="16" viewBox="0 0 10 16"><path d="M8 2 2 8l6 6" fill="none" stroke="#999" stroke-width="2"/></svg>
    <span class="cal-month">AUGUST 2014</span>
    <svg width="10" height="16" viewBox="0 0 10 16"><path d="M2 2l6 6-6 6" fill="none" stroke="#999" stroke-width="2"/></svg>
  </div>
  <div class="cal-grid">
    <span class="dow">Mo</span><span class="dow">Tu</span><span class="dow">We</span><span class="dow">Th</span><span class="dow">Fr</span><span class="dow">Sa</span><span class="dow">Su</span>
    <span class="off">29</span><span class="off">30</span><span class="off">31</span><span>1</span><span>2</span><span>3</span><span>4</span>
    <span>5</span><span>6</span><span>7</span><span>8</span><span>9</span><span>10</span><span>11</span>
    <span>12</span><span class="dot">13</span><span>14</span><span>15</span><span>16</span><span>17</span><span class="mark">18</span>
    <span>19</span><span>20</span><span>21</span><span>22</span><span class="today dot">23</span><span>24</span><span>25</span>
    <span>26</span><span>27</span><span>28</span><span>29</span><span>30</span><span>31</span><span class="off">1</span>
  </div>
</div>

<div class="audience-band"></div>
<article class="audience-card" style="left:162px">
  <svg class="accent" viewBox="0 0 150 194"><polygon points="0,0 130,0 60,194 0,194" fill="#b0141b"/></svg>
  <div class="icon" role="img" aria-label="House icon with owner figure"></div>
  <h3>Direct Owners</h3>
  <p>If you want to manage all aspects of your properties, if you want to publish them on the most famous portals, if you want to create websites for your properties, check what we offer!</p>
  <span class="btn-small">View More</span>
</article>
<article class="audience-card" style="left:612px">
  <svg class="accent" viewBox="0 0 150 194"><polygon points="0,0 130,0 60,194 0,194" fill="#b0141b"/><polygon points="130,0 150,0 150,40 95,194 60,194" fill="#e8a9ab"/></svg>
  <div class="icon" role="img" aria-label="Office building icon with agent figure"></div>
  <h3>Agencies &amp; Portals</h3>
  <p>Discover how we can help you managing data and reservations for the properties you deal with, all your correspondence, all your affiliates, your web presentation and more!</p>
</article>

<section>
  <h2 class="intro-title">Professional Vacation &amp; Villa Rental Management Software</h2>
  <svg class="intro-divider" width="30" height="70" viewBox="0 0 30 70"><line x1="28" y1="2" x2="2" y2="68" stroke="#ccc"/></svg>
  <p class="intro-lead">StayQuill has the best solutions for managing every aspect of villa and vacation rental homes. Built from the ground up around the industry. It is designed to deal with all the day-to-day operations of booking, managing reservations, customer service, communications with clients and owners and more.</p>
  <div class="intro-body">
    <p>StayQuill software is fully integrated into your website both on the front-end and back-end. We make it easy for you to manage both your website and reservations with a seamless solution. Search Engine Optimization (SEO) has been designed into the software enabling you to manage the SEO internally or externally with a consulting firm.</p>
    <p>The software is the ultimate solution for management agencies, booking offices, reservation centers, groups of owners and associations who want to manage their business, clients and customers in a professional manner.</p>
    <p>If you are looking for an affordable professional solution to manage any number of villa or vacation rental properties, please take a look at our StayQuill Software. You'll be glad you did!</p>
    <p>Harbor Lets Ltd recently implemented StayQuill software on their websites including the Hillside Villas and Coastline Villas rental websites and saw a 150% increase in their conversion rate.</p>
  </div>
</section>

<div class="product" style="left:170px">
  <div class="pic" role="img" aria-label="Card payment terminal illustration" style="background:linear-gradient(135deg,#7a5aa8,#cfcfcf)"></div>
  <h4>Virtual POS</h4>
  <p>The easiest and cheapest way to collect the rent amounts and to manage the security deposits</p>
  <div class="plus"><svg width="10" height="10"><path d="M5 0v10M0 5h10" stroke="#333" stroke-width="2"/></svg></div>
</div>
<div class="product" style="left:470px">
  <div class="pic" role="img" aria-label="House with owner illustration" style="background:linear-gradient(135deg,#c8302a,#e3c29a)"></div>
  <h4>Direct Owners</h4>
  <p>" A fully integrated system for managing vacation rentals by a single owner. "</p>
  <div class="plus"><svg width="10" height="10"><path d="M5 0v10M0 5h10" stroke="#333" stroke-width="2"/></svg></div>
</div>
<div class="product" style="left:770px">
  <div class="pic" role="img" aria-label="Office building with agent illustration" style="background:linear-gradient(135deg,#8fb3d0,#b0141b)"></div>
  <h4>Agencies and Portals</h4>
  <p>" A fully integrated system for Vacation Rentals Management designed for Agencies and Portals. "</p>
  <div class="plus"><svg width="10" height="10"><path d="M5 0v10M0 5h10" stroke="#333" stroke-width="2"/></svg></div>
</div>

<section class="testimonials" role="img" aria-label="Dimmed photograph of a villa terrace behind customer testimonials">
  <h2>Testimonials</h2>
  <div class="quote-mark">“</div>
  <blockquote>"Lorem ipsum dolor sit amet, consectetur adipisicing elit, sed do eiusmod tempor incididunt ut labore et dolore magna aliqua. Ut enim ad minim veniam, quis nostrud exercitation ullamco laboris nisi ut aliquip ex ea commodo consequat. Duis aute irure dolor in reprehenderit in voluptate velit esse cillum dolore eu fugiat nulla pariatur. Excepteur sint occaecat cupidatat non proident, sunt in culpa qui officia deserunt mollit anim id est laborum."</blockquote>
  <div class="avatar" role="img" aria-label="Customer portrait"></div>
  <div class="author">Daniel Marsh</div>
</section>

<section>
  <h2 class="portfolio-title">Portfolio</h2>
  <svg class="portfolio-divider" width="30" height="70" viewBox="0 0 30 70"><line x1="28" y1="2" x2="2" y2="68" stroke="#ccc"/></svg>
  <p class="portfolio-lead">We created our procedures by following agencies and owners who operates worldwide since many years in the holiday homes, villas, apartments and residences sector. In addition to this, to increase our services, we got close collaborations with the most famous vacation rentals portals.</p>
  <div class="tile" style="left:162px;background:var(--red)">Harbor Lets</div>
  <div class="tile light" style="left:462px">Marvello Villas</div>
  <div class="tile" style="left:761px;background:var(--red)">Colline Homes</div>
  <div class="tile-caption" style="left:162px">Harbor Lets Ltd, Galway, Ireland</div>
  <div class="tile-caption" style="left:462px">Casali Srl, Certaldo, Italy</div>
  <div class="tile-caption" style="left:761px">Colline Homes GmbH, Kempten, Germany</div>
  <span class="btn-center">View More</span>
</section>

<div class="rule"></div>

<section>
  <h2 class="contact-title">Get In Touch</h2>
  <div class="field active" style="left:162px;top:2177px;width:277px">Name</div>
  <div class="field" style="left:462px;top:2177px;width:277px">Email</div>
  <div class="field" style="left:162px;top:2230px;width:277px">Phone</div>
  <div class="field" style="left:462px;top:2230px;width:277px">Subject</div>
  <div class="field" style="left:162px;top:2282px;width:577px;height:126px">Message</div>
  <div class="submit">Send Message</div>

  <div class="contact-list">
    <div class="contact-item"><svg width="18" height="18" viewBox="0 0 24 24"><path d="M6 3l4 4-2 3c1 3 3 5 6 6l3-2 4 4-3 3C10 21 3 14 3 6z" fill="#555"/></svg><span>+44 5550 123</span></div>
    <div class="contact-item"><svg width="20" height="16" viewBox="0 0 20 16"><rect x="1" y="1" width="18" height="14" fill="none" stroke="#555" stroke-width="1.6"/><path d="M1 1l9 8 9-8" fill="none" stroke="#555" stroke-width="1.6"/></svg><span>info@stayquill.example</span></div>
    <div class="contact-item"><svg width="20" height="22" viewBox="0 0 20 22"><rect x="1" y="1" width="18" height="20" rx="3" fill="none" stroke="#555" stroke-width="1.6"/><path d="M10 5a4 4 0 0 1 4 4c0 3-4 7-4 7s-4-4-4-7a4 4 0 0 1 4-4z" fill="#555"/></svg><span>Lorem ipsum dolor sit,<br>consectetur adipisicing elit,<br>2345687 NL</span></div>
    <div class="socials"><span></span><span></span><span></span></div>
  </div>
</section>

<footer class="site-footer">Copyright © 2014 StayQuill. All Rights Reserved</footer>

</body>
</html>
```